WATTLE HILL PRIMARY SCHOOL - WHPS STATIONARY and Promo Pack

Stationary Design

We are a Western Australian Independent Public Primary School called Wattle Hill Primary School.

We are looking for a new fresh and modern stationary design that reflects our innovative open minded approach.

The school colours are in the teak, turquoise range, basically ocean colours as the school is literally 3 minutes away from the beach and has ocean views.

Feel free to incorporate the school motto: Be Your Best
Feel also free to incorporate our values: Respect, Resilience, Cooperation, Responsibility, Tolerance and Excellence

LIST of DELIVERABLES:

#1: Brand identity elements:
• business card

• stationary - basic package including

o letterhead (print ready)
o envelope design
 DL 110 x 220
 DLX 120 x 235
 A4 229 x 324 and (all print ready)
o template for invoices (delivered as PDF file and Word file)
o cover page for annual report (digital file)
o Notepad A4

• PowerPoint template (delivered as PP file)

• Social media banners & logo avatars (delivered as digital files. Facebook, twitter, pinterest, instagram, google plus)

• With compliment slip (DL size - 210mmx 99mm)

• Thank you card (A6)

• A2 poster background (420mm x 594mm)

#2: Brand promotion elements:

• Staff -T - shirt design - long sleeve and short sleeve polo - (Delivered as mock up and digital file / vector)

• Sport banner (roughly 1800mm x 3000) – needs to be in a darker colour please

• Featherbanner (196 x600mm) compare sketch

Industry/Entity Type

School

Contact Information for Business Card

compare provided sample - all info on that one needs to be used please

Colors
85abd2
0355a3
85acd3
eaf1f7
00a990
33b8a4
87cfc6
cfeae6
cee9f5

Requirements
Must have
• LIST of DELIVERABLES:
• #1: Brand identity elements:
• • business card
• • stationary - basic package including
• o letterhead (print ready)
• o envelope design
•  DL 110 x 220
•  DLX 120 x 235
•  A4 229 x 324 and (all print ready)
• o template for invoices (delivered as PDF file and Word file)
• o cover page for annual report (digital file)
• o Notepad A4
• • PowerPoint template (delivered as PP file)
• • Social media banners & logo avatars (delivered as digital files. Facebook, twitter, pinterest, instagram, google plus)
• • With compliment slip (DL size - 210mmx 99mm)
• • Thank you card (A6)
• • A2 poster background (420mm x 594mm)
• #2: Brand promotion elements:
• • Staff -T - shirt design - long sleeve and short sleeve polo - (Delivered as mock up and digital file / vector)
• • Sport banner (roughly 1800mm x 3000) – needs to be in a darker colour please
• • Featherbanner (196 x600mm) compare sketch

```html
<!DOCTYPE html>
<html lang="en">
<head>
<meta charset="utf-8">
<title>Wattle Hill Primary School – Business Card</title>
<link rel="stylesheet" href="https://fonts.googleapis.com/css2?family=Italianno&family=Cinzel&family=Didact+Gothic&family=Dancing+Script&family=Open+Sans:ital@1&display=swap">
<style>
  :root {
    --teal: #00a595;
    --navy: #001f3a;
    --navy-deep: #00161c;
    --name-band: #48be94;
    --name-fold: #0f6b5d;
    --school-band: #5fbfad;
    --school-fold: #4a9485;
    --mint-text: #7fd6b5;
    --role-text: #5cc5a3;
    --script-ink: #0e4a3e;
    --ink: #0e3a4a;
    --logo-ink: #0d2b55;
    --wave-light: #4b7384;
    --wave-dark: #2f5a6b;
  }
  html, body {
    margin: 0;
    padding: 0;
    overflow: hidden;
    background: #ffffff;
  }
  .card {
    position: relative;
    width: 1200px;
    height: 741px;
    overflow: hidden;
    background: var(--teal);
  }
  .card-shapes {
    position: absolute;
    inset: 0;
  }
  .card-text {
    position: absolute;
    margin: 0;
    white-space: nowrap;
  }
  .staff-email {
    left: 0;
    width: 580px;
    top: 112px;
    text-align: center;
    font: 23px "Didact Gothic", sans-serif;
    color: var(--mint-text);
  }
  .staff-name {
    left: 0;
    width: 580px;
    top: 140px;
    text-align: center;
    font: 86px "Italianno", cursive;
    color: var(--script-ink);
    line-height: 1.25;
  }
  .staff-role {
    left: 0;
    width: 560px;
    top: 270px;
    text-align: center;
    font: 21px "Cinzel", serif;
    color: var(--role-text);
  }
  .school-name {
    right: 92px;
    top: 376px;
    font: 50px "Didact Gothic", sans-serif;
    letter-spacing: 1.5px;
    color: var(--ink);
  }
  .school-tagline {
    right: 92px;
    top: 450px;
    font: 21px "Dancing Script", cursive;
    color: var(--ink);
  }
  .contact-list {
    position: absolute;
    right: 92px;
    top: 482px;
    margin: 0;
    padding: 0;
    list-style: none;
    text-align: right;
    font: italic 26px "Open Sans", sans-serif;
    color: var(--ink);
    line-height: 37.5px;
  }
  .school-mark {
    position: absolute;
    left: 830px;
    top: 80px;
    width: 220px;
    text-align: center;
    color: var(--logo-ink);
    font: 34px "Didact Gothic", sans-serif;
    letter-spacing: 3px;
    line-height: 1.15;
  }
  .school-mark-dot {
    display: block;
    width: 110px;
    height: 110px;
    margin: 0 auto 14px;
    border-radius: 50%;
    background: var(--logo-ink);
  }
</style>
</head>
<body>
<main class="card">
  <svg class="card-shapes" width="1200" height="741" viewBox="0 0 1200 741" aria-hidden="true">
    <defs>
      <linearGradient id="wave-tone" x1="0" y1="0" x2="1" y2="1">
        <stop offset="0" stop-color="var(--wave-light)"/>
        <stop offset="1" stop-color="var(--wave-dark)"/>
      </linearGradient>
    </defs>
    <polygon class="navy-panel" points="0,0 552,0 405,741 0,741" fill="var(--navy)"/>
    <polygon class="name-band-fold" points="498,258 562,258 498,281" fill="var(--name-fold)"/>
    <rect class="name-band" x="0" y="150" width="562" height="108" fill="var(--name-band)"/>
    <polygon class="school-band-fold" points="343,442 470,442 525,490 525,545" fill="var(--school-fold)"/>
    <rect class="school-band" x="343" y="368" width="857" height="74" fill="var(--school-band)"/>
    <polygon class="base-strip" points="0,708 370,708 405,741 0,741" fill="var(--navy-deep)"/>
  </svg>

  <svg class="card-shapes" width="1200" height="741" viewBox="0 0 1200 741" role="img" aria-label="Decorative ocean wave artwork in slate blue tones">
    <path d="M0,360 Q200,330 300,440 Q330,520 300,600 L330,708 L0,708 Z" fill="url(#wave-tone)" opacity="0.9"/>
  </svg>

  <p class="card-text staff-email">Laura.penfold@wattlehill.wa.edu.au</p>
  <p class="card-text staff-name">Laura Penfold</p>
  <p class="card-text staff-role">Registrar</p>

  <div class="school-mark">
    <span class="school-mark-dot"></span>
    WATTLE HILL<br>PRIMARY
  </div>

  <p class="card-text school-name">Wattle Hill Primary School</p>
  <p class="card-text school-tagline">An Independent Public School</p>
  <ul class="contact-list">
    <li>Banksia Road,</li>
    <li>Halls Bay, WA 6210</li>
    <li>Telephone: (08) 9555 0142</li>
    <li>Facsimile: (08) 9555 0143</li>
    <li>Mobile Phone: 0400 555 218</li>
  </ul>
</main>
</body>
</html>
```